E-Commerce Website Update for Bamboo Poles Company

Existing website at:

http://www.reedcraftstudio.example/
http://www.reedcraftstudio.example/pages/product-and-price-list

Two pages to design: home page and "price list" page.

Info for home page as follows:

HOME PAGE:

Header:
Company Name: reedcraft studio
Telephone: 1 888 412 5093

Across the top:
Home | Price List | Blog | FAQ | About | Contact

Down the side:
About Bamboo
Wedding Arbors
Bamboo For Flutes
Black Bamboo
Spotted Bamboo
Bamboo Carpentry
Photo Gallery
All Products & Prices
Blog
FAQ
About
Contact

Should have shopping cart and search buttons on top.
Please see ai file, attached for logo (leaf) and font
In addition the homepage should have one or two sections for promotions

Chosen design will be asked to help deign a PRODUCT AND PRICE LIST page similar to the one we have now, but with "LEARN MORE" and "ORDER NOW" buttons for each item.
Updates

Reason: Thanks  for all the designs so far; giving an extra week for extra consideration.

Target Market(s)

Consumers, wedding planners.

Industry/Entity Type

Shopping

Requirements
Must have
• Clean, easy to read design.
Should not have
• No flash animation.

```html
<!DOCTYPE html>
<html lang="en">
<head>
<meta charset="utf-8">
<title>Reedcraft Studio – Bamboo Poles</title>
<link href="https://fonts.googleapis.com/css2?family=Open+Sans:wght@400;600;700&display=swap" rel="stylesheet">
<style>
:root{
  --leaf:#8cc63e;
  --leaf-dark:#5f8f1f;
  --leaf-deep:#3f6412;
  --ink:#333333;
  --muted:#777777;
  --line:#dddddd;
  --panel:#f4f4f4;
  --footer:#3a3a3a;
  --footer-text:#bbbbbb;
  --cane:#c9b27a;
  --cane-dark:#8a7444;
}
*{box-sizing:border-box;margin:0;padding:0}
html,body{width:855px;height:1200px;overflow:hidden}
body{font-family:"Open Sans",Arial,sans-serif;color:var(--ink);background:#fff;position:relative;font-size:10px}
.page{position:absolute;left:97px;top:0;width:660px;height:870px}
.brand{position:absolute;left:0;top:22px;display:flex;align-items:center;gap:8px;font-size:26px;font-weight:700;color:var(--leaf-dark);letter-spacing:-.5px}
.brand-dot{width:16px;height:16px;border-radius:50%;background:var(--leaf)}
.phone{position:absolute;right:0;top:26px;display:flex;align-items:center;gap:8px;font-size:24px;font-weight:700;color:var(--ink)}
.main-nav{position:absolute;left:0;top:80px;width:660px;height:24px;background:linear-gradient(var(--leaf),var(--leaf-dark));display:flex}
.main-nav a{color:#fff;text-decoration:none;font-size:10px;font-weight:600;padding:0 14px;line-height:24px}
.main-nav a.active{background:#2e2e2e}
.toolbar{position:absolute;right:0;top:112px;display:flex;align-items:center;gap:6px;font-size:9px;color:var(--muted)}
.toolbar .select,.toolbar .search{border:1px solid var(--line);height:16px;line-height:14px;padding:0 4px;color:var(--muted)}
.toolbar .select{width:70px}
.toolbar .search{width:120px}
.toolbar .go{background:var(--leaf-dark);color:#fff;height:16px;line-height:16px;padding:0 6px;font-weight:700}
.toolbar .cart{display:flex;align-items:center;gap:4px;margin-left:6px;color:var(--ink)}
.slider{position:absolute;left:0;top:140px;width:495px;height:200px;background:linear-gradient(160deg,#dfe9ee 0%,#cbb98a 45%,#8e7a4a 100%)}
.slider .arrow{position:absolute;top:70px;width:22px;height:22px;border-radius:50%;background:rgba(0,0,0,.45)}
.slider .arrow.prev{left:8px}.slider .arrow.next{right:8px}
.thumbs{position:absolute;left:8px;right:8px;bottom:6px;display:flex;gap:6px}
.thumb{flex:1;height:44px;background:linear-gradient(var(--cane),var(--cane-dark));position:relative;border:2px solid #fff}
.thumb span{position:absolute;left:0;right:0;bottom:0;background:rgba(0,0,0,.6);color:#fff;font-size:7px;padding:1px 3px;white-space:nowrap;overflow:hidden}
.sidebar{position:absolute;left:510px;top:140px;width:150px}
.side-box{border:1px solid var(--line);margin-bottom:10px}
.side-box h3{background:var(--leaf-dark);color:#fff;font-size:9px;font-weight:700;padding:5px 8px;text-transform:uppercase}
.side-box ul{list-style:none;padding:4px 8px}
.side-box li{font-size:9px;line-height:19px;border-bottom:1px dotted var(--line);padding-left:10px;position:relative}
.side-box li:last-child{border-bottom:0}
.side-box li::before{content:"";position:absolute;left:0;top:7px;border-left:4px solid var(--leaf-dark);border-top:3px solid transparent;border-bottom:3px solid transparent}
.side-photo{height:100px;background:linear-gradient(100deg,var(--cane-dark),var(--cane),#e2d3a6)}
.welcome{position:absolute;left:0;top:352px;width:495px;height:150px}
.welcome h1{font-size:13px;font-weight:700;color:var(--ink);margin-bottom:6px}
.welcome .copy{width:345px}
.welcome p{font-size:8.5px;line-height:13px;color:var(--muted);margin-bottom:6px}
.welcome .photo{position:absolute;right:0;top:20px;width:135px;height:115px;background:linear-gradient(var(--cane),var(--cane-dark))}
.products{position:absolute;left:0;top:512px;width:660px;display:grid;grid-template-columns:repeat(4,150px);column-gap:20px;row-gap:14px}
.product{height:160px;border:1px solid var(--line);padding:5px;display:flex;flex-direction:column}
.product .shot{height:90px;background:linear-gradient(90deg,#e8dcb8,var(--cane),#e8dcb8)}
.product .shot.black{background:linear-gradient(90deg,#6b6b6b,#2a2a2a,#6b6b6b)}
.product .shot.spotted{background:linear-gradient(90deg,#d9c99c,#a88d55,#d9c99c)}
.product .shot.arbor{background:linear-gradient(#e8efe0,#b7a170)}
.product h4{font-size:8.5px;font-weight:600;text-align:center;margin:5px 0;line-height:11px;flex:1}
.product .buy{display:flex;justify-content:space-between;align-items:center}
.product .price{font-size:11px;font-weight:700;color:var(--leaf-deep)}
.btn{background:var(--leaf-dark);color:#fff;font-size:8px;font-weight:700;padding:3px 7px;border-radius:2px}
.footer-band{position:absolute;left:0;top:875px;width:855px;height:250px;background:var(--footer)}
.footer-cols{position:absolute;left:97px;top:18px;width:660px;display:flex;gap:30px}
.footer-col{flex:1;position:relative;height:215px}
.footer-col h2{display:flex;align-items:center;gap:8px;color:#fff;font-size:17px;font-weight:700;margin-bottom:10px}
.footer-col .icon{width:22px;height:22px;border-radius:4px;background:var(--leaf)}
.footer-col p{color:var(--footer-text);font-size:8.5px;line-height:13px}
.post{margin-bottom:12px}
.post h5{color:var(--leaf);font-size:9px;font-weight:700}
.post time{color:#999;font-size:8px;display:block}
.footer-col .btn{position:absolute;right:0;bottom:6px;background:#222;border:1px solid #555}
.bottom{position:absolute;left:0;top:1135px;width:855px;text-align:center}
.bottom nav{font-size:8.5px;color:var(--muted);line-height:14px;padding:0 150px}
.bottom nav a{color:var(--muted);text-decoration:none;margin:0 5px}
.bottom small{display:block;font-size:8px;color:#999;margin-top:6px}
</style>
</head>
<body>
<div class="page">
  <header>
    <div class="brand"><span class="brand-dot"></span>reedcraft studio</div>
    <div class="phone">
      <svg width="20" height="20" viewBox="0 0 24 24"><path fill="#5f8f1f" d="M6.6 10.8a15 15 0 0 0 6.6 6.6l2.2-2.2c.3-.3.7-.4 1-.2 1.1.4 2.3.6 3.6.6.6 0 1 .4 1 1V20c0 .6-.4 1-1 1A17 17 0 0 1 3 4c0-.6.4-1 1-1h3.5c.6 0 1 .4 1 1 0 1.3.2 2.5.6 3.6.1.3 0 .7-.2 1z"/></svg>
      1 888 412 5093
    </div>
  </header>

  <nav class="main-nav">
    <a class="active" href="#">Home</a><a href="#">Price List</a><a href="#">Blog</a><a href="#">FAQ</a><a href="#">About</a><a href="#">Contact</a>
  </nav>

  <div class="toolbar">
    <span>Currency:</span><span class="select">US Dollar ▾</span>
    <span class="search">Search store</span><span class="go">GO</span>
    <span class="cart">
      <svg width="14" height="12" viewBox="0 0 24 20"><path fill="#5f8f1f" d="M0 1h4l3 11h12l3-8H7" stroke="#5f8f1f" stroke-width="2" fill-opacity="0"/><circle cx="9" cy="17" r="2" fill="#5f8f1f"/><circle cx="18" cy="17" r="2" fill="#5f8f1f"/></svg>
      <b>Shopping Cart:</b> 0 items – $0.00
    </span>
  </div>

  <section class="slider" role="img" aria-label="Photo of bundled natural bamboo poles standing against a pale sky">
    <span class="arrow prev"></span><span class="arrow next"></span>
    <div class="thumbs">
      <div class="thumb" role="img" aria-label="Spotted bamboo poles"><span>1.88" x 8' Spotted</span></div>
      <div class="thumb" role="img" aria-label="Natural bamboo poles"><span>10 pcs 1" x 6'</span></div>
      <div class="thumb" role="img" aria-label="Black bamboo poles"><span>Black Bamboo</span></div>
      <div class="thumb" role="img" aria-label="Wide bamboo poles"><span>2 pcs 2" x 8'</span></div>
      <div class="thumb" role="img" aria-label="Bamboo wedding arbor"><span>Wedding Arbor</span></div>
    </div>
  </section>

  <aside class="sidebar">
    <div class="side-box">
      <h3>Bamboo Poles</h3>
      <ul><li>Reed Bamboo</li><li>Tonkin Bamboo</li><li>Moso Bamboo</li><li>Black Bamboo</li><li>Vine Bamboo</li></ul>
    </div>
    <div class="side-box">
      <h3>Bamboo Categories</h3>
      <ul><li>Cutting Bamboo</li><li>Bending Bamboo</li><li>Weave Gift</li><li>Preventing Cracking</li></ul>
    </div>
    <div class="side-photo" role="img" aria-label="Photo of a stack of cut bamboo poles"></div>
  </aside>

  <section class="welcome">
    <h1>Welcome to your Pole Provider 1 888 412 5093</h1>
    <div class="copy">
      <p>Reedcraft Studio has supplied natural bamboo poles to homes, gardens, event planners and craft makers for many years. Every pole is cut, cured and graded by hand, then sorted by size so you receive straight, even stock ready for your project.</p>
      <p>Our poles come in black, spotted and natural tones, in lengths from four to ten feet. Browse the full price list to compare sizes, or call us and we will help you choose.</p>
      <p>Planning a wedding or event? Ask about arbor kits and bulk orders for decorators.</p>
    </div>
    <div class="photo" role="img" aria-label="Photo of long bamboo poles lying in rows"></div>
  </section>

  <section class="products">
    <article class="product"><div class="shot spotted" role="img" aria-label="Spotted bamboo poles"></div><h4>1.75" x 8 feet Spotted Bamboo Poles</h4><div class="buy"><span class="price">$39.00</span><span class="btn">Order Now</span></div></article>
    <article class="product"><div class="shot black" role="img" aria-label="Black bamboo poles"></div><h4>10 pcs 1" x 8' Black Bamboo Poles</h4><div class="buy"><span class="price">$42.00</span><span class="btn">Order Now</span></div></article>
    <article class="product"><div class="shot" role="img" aria-label="Natural bamboo poles"></div><h4>10 pcs 1" x 6' Bamboo Poles</h4><div class="buy"><span class="price">$28.00</span><span class="btn">Order Now</span></div></article>
    <article class="product"><div class="shot arbor" role="img" aria-label="Bamboo wedding arbor in a garden"></div><h4>Bamboo Wedding Arbor</h4><div class="buy"><span class="price">$189.00</span><span class="btn">Order Now</span></div></article>
    <article class="product"><div class="shot" role="img" aria-label="Natural bamboo poles"></div><h4>4 poles 1.88 inch x 8 feet Bamboo Poles</h4><div class="buy"><span class="price">$36.00</span><span class="btn">Order Now</span></div></article>
    <article class="product"><div class="shot" role="img" aria-label="Natural bamboo poles"></div><h4>6 pcs 2" x 8' Bamboo Poles</h4><div class="buy"><span class="price">$54.00</span><span class="btn">Order Now</span></div></article>
    <article class="product"><div class="shot" role="img" aria-label="Natural bamboo poles"></div><h4>2 pcs 2" x 8' 10' Bamboo Poles</h4><div class="buy"><span class="price">$32.00</span><span class="btn">Order Now</span></div></article>
    <article class="product"><div class="shot black" role="img" aria-label="Black bamboo poles"></div><h4>10 pcs 1/8" x 8' Black Bamboo Poles</h4><div class="buy"><span class="price">$44.00</span><span class="btn">Order Now</span></div></article>
  </section>
</div>

<footer>
  <div class="footer-band">
    <div class="footer-cols">
      <div class="footer-col">
        <h2><span class="icon"></span>Our Blog</h2>
        <div class="post"><h5>Bamboo Pole Order</h5><time>March 12</time><p>How to pick the right diameter for a garden trellis.</p></div>
        <div class="post"><h5>Bamboo Pole Finish</h5><time>February 27</time><p>Caring for black bamboo through a dry winter season.</p></div>
        <span class="btn">Read More</span>
      </div>
      <div class="footer-col">
        <h2><span class="icon"></span>About us</h2>
        <p>Reedcraft Studio is a small family business that cuts, cures and ships bamboo poles across the country. We care about quality, fair prices and friendly help with every order, large or small. Poles are graded by hand and packed with care.</p>
        <span class="btn">Read More</span>
      </div>
      <div class="footer-col">
        <h2><span class="icon"></span>Hand Painted</h2>
        <p>Many of our poles can be hand painted with simple patterns or solid colours. Tell us your theme and we will match the finish for weddings, shops and stage sets. Each piece is sealed to last indoors and out.</p>
        <span class="btn">Read More</span>
      </div>
    </div>
  </div>
  <div class="bottom">
    <nav><a href="#">About Bamboo</a>|<a href="#">Wedding Arbors</a>|<a href="#">Bamboo For Flutes</a>|<a href="#">Black Bamboo</a>|<a href="#">Spotted Bamboo</a>|<a href="#">Bamboo Carpentry</a>|<a href="#">Photo Gallery</a>|<a href="#">All Products &amp; Prices</a>|<a href="#">Blog</a>|<a href="#">FAQ</a>|<a href="#">About</a>|<a href="#">Contact</a></nav>
    <small>© 2024 Reedcraft Studio. All Rights Reserved.</small>
  </div>
</footer>
</body>
</html>
```